Coffee Package Design

We need a new package design for a coffee company. Need to be a mix between modern and classic design combined together. We are open to different ideas.
We changing our product name from Café Verlona to Café Rostelli. The picture upload
shows what the product looks like. We want something completely different. The name of the company should go on the back of the package.
Updates

Hello Everyone,

Please read description, we are going with a new name and design for the product.

Café Rostelli. Café Verlona is what we are replacing with Café Rostelli, we are looking for new

look and design, please submit new designs.

There is a change in the description. Please take out Premium coffee blend and replace with Italian Roast.                                    

Industry/Entity Type

Cafe

Requirements
Must have
• You can use up to 6 colors.
Please put these items on design: Café Rostelli (this is the product name), Regular Premium Blend Coffee, 100% Arabica,
Dumbrell & Sons (name of the company), Marlow, OK on the back of the package

The file uploaded is an example of one of our products and how the package film
is sized.

```html
<!DOCTYPE html>
<html lang="en">
<head>
<meta charset="utf-8">
<title>Café Rostelli – Coffee Package Film Layout</title>
<link rel="stylesheet" href="https://fonts.googleapis.com/css2?family=Merriweather:wght@400;700&family=Source+Sans+3:wght@400&display=swap">
<style>
  :root {
    --film-green: #76cb3b;
    --art-green-light: #c4f08a;
    --ink-dark: #231f20;
    --ink-white: #ffffff;
    --guide-blue: #29a8e0;
    --paper: #ffffff;
  }
  html, body {
    margin: 0;
    padding: 0;
    overflow: hidden;
    background: var(--paper);
  }
  .canvas {
    display: block;
    width: 1200px;
    height: 725px;
  }
  .film { fill: var(--film-green); }
  .guide { stroke: var(--guide-blue); stroke-width: 1; fill: none; }
  .guide-dash { stroke: var(--guide-blue); stroke-width: 1; fill: none; stroke-dasharray: 12 8; }
  .dim-label {
    font-family: "Source Sans 3", sans-serif;
    font-size: 14px;
    fill: var(--guide-blue);
  }
  .dim-label-large {
    font-family: "Source Sans 3", sans-serif;
    font-size: 16px;
    fill: var(--guide-blue);
  }
  .note-label {
    font-family: "Source Sans 3", sans-serif;
    font-size: 13px;
    fill: var(--guide-blue);
  }
  .microdot-label {
    font-family: "Source Sans 3", sans-serif;
    font-size: 8px;
    fill: var(--guide-blue);
  }
  .brand-name {
    font-family: "Merriweather", serif;
    font-weight: 700;
    fill: var(--ink-dark);
  }
  .flavor-title {
    font-family: "Merriweather", serif;
    font-weight: 700;
    font-size: 21px;
    fill: var(--ink-white);
  }
  .flavor-sub {
    font-family: "Merriweather", serif;
    font-weight: 400;
    font-size: 16px;
    fill: var(--ink-white);
    letter-spacing: 0.5px;
  }
  .back-title {
    font-family: "Merriweather", serif;
    font-weight: 700;
    font-size: 14px;
    fill: var(--ink-dark);
  }
  .back-line {
    font-family: "Merriweather", serif;
    font-weight: 400;
    font-size: 12px;
    fill: var(--ink-dark);
  }
  .back-line-small {
    font-family: "Merriweather", serif;
    font-weight: 400;
    font-size: 10px;
    fill: var(--ink-dark);
  }
</style>
</head>
<body>
<svg class="canvas" viewBox="0 0 1200 725" xmlns="http://www.w3.org/2000/svg">
  <defs>
    <radialGradient id="botanical-tone" cx="0.55" cy="0.5" r="0.6">
      <stop offset="0" stop-color="#c4f08a" stop-opacity="0.55"/>
      <stop offset="1" stop-color="#c4f08a" stop-opacity="0"/>
    </radialGradient>
    <marker id="arrow" viewBox="0 0 10 10" refX="10" refY="5" markerWidth="7" markerHeight="7" orient="auto-start-reverse">
      <path d="M0 0 L10 5 L0 10 z" fill="#29a8e0"/>
    </marker>
  </defs>

  <!-- Package film -->
  <rect class="film" x="52" y="52" width="13" height="610"/>
  <rect class="film" x="80" y="44" width="980" height="626"/>
  <rect class="film" x="1060" y="333" width="73" height="48"/>

  <!-- Botanical illustration zone -->
  <rect x="570" y="120" width="440" height="495" fill="url(#botanical-tone)" role="img" aria-label="Light green line illustration of coffee plants, beans and figures wrapping the front and side panels"/>

  <!-- Panel guides -->
  <rect class="guide" x="90" y="52" width="1055" height="610"/>
  <line class="guide" x1="173" y1="52" x2="173" y2="662"/>
  <line class="guide" x1="376" y1="52" x2="376" y2="662"/>
  <line class="guide-dash" x1="617" y1="52" x2="617" y2="662"/>
  <line class="guide" x1="857" y1="52" x2="857" y2="662"/>
  <line class="guide-dash" x1="48" y1="124" x2="1145" y2="124"/>
  <line class="guide-dash" x1="48" y1="613" x2="1145" y2="613"/>

  <!-- Top dimensions -->
  <g class="top-dimensions">
    <line class="guide" x1="90" y1="0" x2="90" y2="44"/>
    <line class="guide" x1="173" y1="0" x2="173" y2="44"/>
    <line class="guide" x1="376" y1="0" x2="376" y2="44"/>
    <line class="guide" x1="617" y1="0" x2="617" y2="44"/>
    <line class="guide" x1="857" y1="0" x2="857" y2="44"/>
    <line class="guide" x1="1060" y1="0" x2="1060" y2="44"/>
    <line class="guide" x1="1145" y1="0" x2="1145" y2="44"/>
    <text class="dim-label" x="131" y="25" text-anchor="middle">.875″</text>
    <text class="dim-label" x="274" y="25" text-anchor="middle">2.125″</text>
    <text class="dim-label" x="496" y="25" text-anchor="middle">2.50″</text>
    <text class="dim-label" x="737" y="25" text-anchor="middle">2.50″</text>
    <text class="dim-label" x="958" y="25" text-anchor="middle">2.125″</text>
    <text class="dim-label" x="1102" y="25" text-anchor="middle">.875″</text>
  </g>

  <!-- Side seal dimensions -->
  <text class="dim-label" x="24" y="94">.75″</text>
  <text class="dim-label" x="24" y="645">.50″</text>

  <!-- Web width -->
  <line class="guide" x1="92" y1="682" x2="1143" y2="682" marker-start="url(#arrow)" marker-end="url(#arrow)"/>
  <text class="dim-label-large" x="617" y="703" text-anchor="middle">Web Width 11.00″</text>

  <!-- Cylinder / repeat -->
  <line class="guide" x1="1145" y1="52" x2="1178" y2="52"/>
  <line class="guide" x1="1145" y1="662" x2="1178" y2="662"/>
  <line class="guide" x1="1163" y1="56" x2="1163" y2="658" marker-start="url(#arrow)" marker-end="url(#arrow)"/>
  <text class="dim-label-large" transform="translate(1190 356) rotate(-90)" text-anchor="middle">Cylinder size 19.094″ Repeat 6.3647″</text>

  <!-- Eyetrack note -->
  <text class="note-label" transform="translate(1092 598) rotate(-90)">Eyetrack needs to be white.</text>
  <text class="note-label" transform="translate(1108 598) rotate(-90)">Eyespot .75″ x .50″ centered</text>
  <text class="note-label" transform="translate(1124 598) rotate(-90)">in between cutoffs.</text>

  <!-- Microdots -->
  <g class="microdots">
    <circle class="guide" cx="112" cy="50" r="2.5"/>
    <line class="guide" x1="78" y1="43" x2="109" y2="48"/>
    <text class="microdot-label" x="32" y="43">microdot</text>

    <circle class="guide" cx="1122" cy="50" r="2.5"/>
    <line class="guide" x1="1158" y1="43" x2="1125" y2="48"/>
    <text class="microdot-label" x="1158" y="45">microdot</text>

    <circle class="guide" cx="112" cy="357" r="2.5"/>
    <line class="guide" x1="84" y1="340" x2="109" y2="355"/>
    <text class="microdot-label" transform="translate(80 338) rotate(-90)">microdot</text>

    <circle class="guide" cx="1121" cy="356" r="2.5"/>
    <line class="guide" x1="1121" y1="318" x2="1121" y2="353"/>
    <text class="microdot-label" x="1088" y="316">microdot</text>
  </g>

  <!-- Side panel brand name (vertical) -->
  <text class="brand-name" font-size="38" transform="translate(288 380) rotate(-90)" text-anchor="middle" textLength="225" lengthAdjust="spacingAndGlyphs">Café Rostelli</text>

  <!-- Front panel -->
  <g class="front-panel">
    <circle cx="478" cy="335" r="5" fill="var(--ink-dark)"/>
    <text class="brand-name" font-size="38" x="494" y="349" textLength="236" lengthAdjust="spacingAndGlyphs">Café Rostelli</text>
    <text class="flavor-title" x="473" y="459">Italian Roast</text>
    <text class="flavor-sub" x="473" y="487">100% Arabica</text>
  </g>

  <!-- Back panel -->
  <g class="back-panel">
    <text class="back-title" transform="translate(947 485) rotate(-90)">Café Rostelli</text>
    <text class="back-line" transform="translate(964 485) rotate(-90)">Italian Roast, 100% Arabica</text>
    <text class="back-line-small" transform="translate(986 485) rotate(-90)">Dumbrell &amp; Sons, Marlow, OK</text>
  </g>
</svg>
</body>
</html>
```